Cognitive therapist.

I am a therapist and my main work is with clients who have depression and anxiety disorders.

I need something reasonably plain. Larnwood Therapy is a very pragmatic approach to dealing with problems, so it isn't new agey (no offence to new age therapies at all)

Hi everyone, I am currently looking at a particular design that I will most likely go with. Cheers, Mel

Mel Tarrow
Cognitive Therapist
BA, PG Dip Mental Health,
PG Dip Cog Beh Therapy
MKLPT

The Larchmont Rooms,
Level One
57 Quillon Parade
Cnr Fenwick St & Quillon Parade
P O Box 38 215
WELLINGTON 6281

Phone: 027 534 2870 Email: mtarrow@vexmail.co.nz

www.meltarrow.co.nz

• No illustration, or colour. not old style fonts.

```html
<!DOCTYPE html>
<html lang="en">
<head>
<meta charset="utf-8">
<title>Larnwood Therapy – Business Card</title>
<link rel="stylesheet" href="https://fonts.googleapis.com/css2?family=Open+Sans:wght@300;400&family=Exo+2:wght@500&display=swap">
<style>
  :root {
    --backdrop: #a4a5a7;
    --card: #ffffff;
    --card-shade: #eef0f1;
    --cyan: #1fb0ea;
    --name-blue: #2f7cc0;
    --slate: #8b8e92;
    --ink: #3a3c40;
  }
  * { box-sizing: border-box; margin: 0; padding: 0; }
  html, body { width: 1200px; height: 894px; overflow: hidden; }
  body {
    background: var(--backdrop);
    font-family: "Open Sans", Arial, sans-serif;
    position: relative;
  }
  .card {
    position: absolute;
    left: 280px;
    width: 640px;
    height: 366px;
    background: linear-gradient(135deg, var(--card) 40%, var(--card-shade));
    overflow: hidden;
  }
  .card--front { top: 50px; }
  .card--back { top: 470px; }

  .frame {
    position: absolute;
    inset: 26px 34px;
    border: 3px solid var(--cyan);
    z-index: 2;
  }
  .band {
    position: absolute;
    left: 0; right: 0;
    background: var(--cyan);
  }
  .card--front .band { top: 258px; height: 54px; }
  .card--back .band { top: 296px; height: 44px; }

  .brand {
    position: absolute;
    color: var(--cyan);
    font-weight: 300;
    white-space: nowrap;
  }
  .card--front .brand {
    left: 0; right: 0; top: 118px;
    text-align: center;
    font-size: 46px;
  }
  .card--back .brand {
    left: 60px; top: 46px;
    font-size: 34px;
  }

  .band-url {
    position: absolute;
    left: 0; right: 0; top: 270px;
    text-align: center;
    color: #fff;
    font-size: 20px;
    letter-spacing: 2px;
    z-index: 3;
  }

  .side-block {
    position: absolute;
    left: 0; top: 262px;
    width: 118px; height: 34px;
    background: var(--slate);
    clip-path: polygon(0 0, 88% 0, 100% 100%, 0 100%);
  }

  .contact {
    position: absolute;
    display: flex;
    align-items: flex-start;
    gap: 12px;
    font-size: 16px;
    line-height: 1.3;
    color: var(--ink);
    white-space: nowrap;
  }
  .contact svg { flex: none; width: 22px; height: 22px; }
  .contact--phone { left: 62px; top: 118px; }
  .contact--email { left: 62px; top: 154px; }
  .contact--address { left: 352px; top: 212px; }
  .contact--web { left: 352px; top: 258px; }

  .person {
    position: absolute;
    right: 70px; top: 146px;
    text-align: left;
  }
  .person__name {
    font-family: "Exo 2", Arial, sans-serif;
    font-weight: 500;
    color: var(--name-blue);
    font-size: 22px;
    letter-spacing: 1px;
  }
  .person__role {
    font-family: "Exo 2", Arial, sans-serif;
    color: var(--ink);
    font-size: 14px;
  }
</style>
</head>
<body>

<section class="card card--front">
  <div class="frame"></div>
  <div class="band"></div>
  <h1 class="brand">Larnwood Therapy</h1>
  <p class="band-url">www.yoursitename.com</p>
</section>

<section class="card card--back">
  <div class="frame"></div>
  <div class="side-block"></div>
  <div class="band"></div>
  <h2 class="brand">Larnwood Therapy</h2>

  <p class="contact contact--phone">
    <svg viewBox="0 0 22 22" aria-hidden="true"><rect width="22" height="22" rx="4" fill="#1fb0ea"/><path d="M7 5c1 0 1.6 2.4 1.2 3-.4.5-1 .7-.6 1.6.7 1.5 1.9 2.7 3.4 3.4.9.4 1.1-.2 1.6-.6.6-.4 3 .2 3 1.2 0 1.3-1.2 2.4-2.6 2.2C8.8 17.2 4.8 13.2 4.6 8 4.6 6.2 5.8 5 7 5z" fill="#fff"/></svg>
    <span>012 468 2579</span>
  </p>
  <p class="contact contact--email">
    <svg viewBox="0 0 22 22" aria-hidden="true"><rect width="22" height="22" rx="4" fill="#1fb0ea"/><rect x="5" y="7" width="12" height="8" fill="#fff"/><path d="M5 7l6 5 6-5" fill="none" stroke="#1fb0ea" stroke-width="1.2"/></svg>
    <span>yourname@mailbox.com</span>
  </p>

  <div class="person">
    <p class="person__name">Dale Morven</p>
    <p class="person__role">Production engineer</p>
  </div>

  <p class="contact contact--address">
    <svg viewBox="0 0 22 22" aria-hidden="true"><rect width="22" height="22" rx="4" fill="#1fb0ea"/><path d="M11 4a5 5 0 0 1 5 5c0 3.5-5 9-5 9s-5-5.5-5-9a5 5 0 0 1 5-5z" fill="#fff"/><circle cx="11" cy="9" r="1.8" fill="#1fb0ea"/></svg>
    <span>041.12th floor,Park<br>Ridgeway Road KLM</span>
  </p>
  <p class="contact contact--web">
    <svg viewBox="0 0 22 22" aria-hidden="true"><rect width="22" height="22" rx="4" fill="#1fb0ea"/><circle cx="11" cy="11" r="6" fill="none" stroke="#fff" stroke-width="1.4"/><ellipse cx="11" cy="11" rx="2.5" ry="6" fill="none" stroke="#fff" stroke-width="1.2"/><path d="M5 11h12" stroke="#fff" stroke-width="1.2"/></svg>
    <span>www.yoursitename.com</span>
  </p>
</section>

</body>
</html>
```